web site update

I want to get a better website for a small high end remodeling and construction company
I currently have a web site but you will find that it is not good.
www.quenbrickhall.com
We are a high end construction / remodeling company that has been in business since 2003. We primarily work in the mid peninsula of the bay area. Most of our clientele are very educated captains of industry. This group is still the target client.
I had my logo designed by Mint Easel a few years ago and I do like it, I like the orange and black or orange a blue. I don’t have a lot of content on hand as far as professional photographs.
Number of pages not sure and are open to: design pages vs full function website
I think what I am after is a web presence that will seal the deal as we are getting high referrals from past clients.
Construction
1 page

```html
<!DOCTYPE html>
<html lang="en">
<head>
<meta charset="utf-8">
<title>Quenbrick Hall Remodeling</title>
<link href="https://fonts.googleapis.com/css2?family=Open+Sans:wght@400;600;700;800&display=swap" rel="stylesheet">
<style>
  :root {
    --orange: #ff6600;
    --black: #000000;
    --white: #ffffff;
    --ink: #111111;
    --body-grey: #666666;
    --band-grey: #e6e6e6;
    --rule: #8a4a4a;
    --portrait-light: #f4f4f4;
    --portrait-mid: #9a9a9a;
  }
  * { margin: 0; padding: 0; box-sizing: border-box; }
  html, body { width: 1200px; height: 1121px; overflow: hidden; }
  body {
    position: relative;
    background: var(--white);
    font-family: "Open Sans", Arial, sans-serif;
    color: var(--body-grey);
  }
  .site-header { position: absolute; left: 0; top: 0; width: 1200px; height: 154px; }
  .brand { position: absolute; left: 156px; top: 30px; display: flex; align-items: center; gap: 16px; }
  .brand-square { width: 74px; height: 74px; background: var(--black); }
  .brand-name {
    color: var(--orange); font-weight: 800; font-size: 22px; line-height: 24px; letter-spacing: 1px;
  }
  .brand-name small { display: block; font-size: 15px; letter-spacing: 2px; }
  .main-nav { position: absolute; top: 57px; left: 752px; display: flex; font-size: 13.5px; color: var(--ink); }
  .main-nav span { position: absolute; white-space: nowrap; letter-spacing: 0.3px; }
  .header-phone {
    position: absolute; left: 797px; top: 94px; font-size: 32px; font-weight: 700; color: var(--orange);
  }
  .hero { position: absolute; left: 0; top: 154px; width: 1200px; height: 293px; background: var(--orange); }
  .hero-title {
    position: absolute; left: 216px; top: 96px; color: var(--white);
    font-size: 31px; line-height: 31px; font-weight: 700; letter-spacing: 1.4px;
  }
  .hero-art {
    position: absolute; left: 651px; top: 5px; width: 378px; height: 280px;
    background: linear-gradient(160deg, rgba(255,255,255,0.18), rgba(255,255,255,0.05));
  }
  .services { position: absolute; top: 471px; left: 0; width: 1200px; }
  .service { position: absolute; width: 255px; }
  .service-head {
    display: flex; align-items: flex-end; gap: 8px; height: 35px; padding-bottom: 3px;
    border-bottom: 1px solid var(--rule); color: var(--ink); font-size: 15px; font-weight: 400;
  }
  .service-mark { width: 24px; height: 24px; background: var(--black); margin-left: 2px; }
  .service p { font-size: 12.4px; line-height: 14.4px; margin-top: 14px; }
  .service p + p { margin-top: 14px; }
  .meet { position: absolute; left: 0; top: 697px; width: 1200px; height: 254px; background: var(--band-grey); }
  .meet-title { position: absolute; left: 187px; top: 32px; color: var(--orange); font-size: 21px; font-weight: 800; letter-spacing: 1px; }
  .meet-text { position: absolute; left: 216px; top: 66px; width: 500px; font-size: 12.4px; line-height: 14.4px; color: #555; }
  .meet-text p + p { margin-top: 14px; }
  .read-more { position: absolute; left: 617px; top: 224px; color: var(--orange); font-size: 12px; font-weight: 700; }
  .portrait {
    position: absolute; left: 768px; top: 24px; width: 194px; height: 194px; border-radius: 50%;
    background: radial-gradient(circle at 50% 45%, var(--portrait-mid) 0 45%, var(--portrait-light) 75%);
  }
  .site-footer { position: absolute; left: 0; top: 951px; width: 1200px; height: 170px; background: var(--black); color: var(--white); }
  .footer-contact { position: absolute; left: 172px; top: 40px; font-size: 12.5px; line-height: 16px; letter-spacing: 0.4px; }
  .footer-contact p + p { margin-top: 16px; }
  .galleries-title { position: absolute; left: 455px; top: 35px; color: var(--orange); font-size: 14px; font-weight: 600; letter-spacing: 0.5px; }
  .gallery-list { position: absolute; top: 70px; list-style: none; font-size: 12.5px; line-height: 14.5px; letter-spacing: 0.5px; color: #dddddd; }
  .social { position: absolute; top: 41px; left: 800px; display: flex; gap: 19px; }
  .social-square { width: 39px; height: 39px; background: var(--orange); }
  .copyright { position: absolute; left: 799px; top: 110px; font-size: 9.5px; font-weight: 700; }
</style>
</head>
<body>
  <header class="site-header">
    <div class="brand">
      <div class="brand-square"></div>
      <div class="brand-name">QUENBRICK<br>HALL<small>REMODELING</small></div>
    </div>
    <nav class="main-nav">
      <span style="left:0">HOME</span>
      <span style="left:71px">ABOUT</span>
      <span style="left:139px">GALLERY ▾</span>
      <span style="left:232px">CONTACT</span>
    </nav>
    <div class="header-phone">415-555-0187</div>
  </header>

  <section class="hero">
    <h1 class="hero-title">YOUR PERSONALCUSTOM<br>RENOVATION AND<br>CONSTRUCTION SPECIALIST</h1>
    <div class="hero-art" role="img" aria-label="White line drawing of a house frame standing on architectural plans"></div>
  </section>

  <section class="services">
    <article class="service" style="left:166px">
      <h2 class="service-head"><span class="service-mark"></span>FEATURED SERVICE</h2>
      <p>Lorem ipsum dolor sit amet, consetetur sadipscing elitr, sed diam nonumy eirmod tempor invidunt ut labore et dolore magna aliquyam erat, sed diam voluptua.</p>
      <p>At vero eos et accusam et justo duo dolores et ea rebum. gubergren, &nbsp;Lorem ipsum dolor sit amet. Lorem ipsum dolor sit amet, consetetur dolore magna.</p>
    </article>
    <article class="service" style="left:472px">
      <h2 class="service-head"><span class="service-mark"></span>FEATURED SERVICE</h2>
      <p>Lorem ipsum dolor sit amet, consetetur sadipscing elitr, sed diam nonumy eirmod tempor invidunt ut labore et dolore magna aliquyam erat, sed diam voluptua. At vero eos et accusam et justo duo dolores et ea rebum. Stet clita kasd gubergren,Lorem ipsum dolor sit amet. Lorem ipsum dolor sit amet, consetetur dolore magna sanctus est Lorem ipsum dolor sit amet.</p>
    </article>
    <article class="service" style="left:777px">
      <h2 class="service-head"><span class="service-mark"></span>FEATURED SERVICE</h2>
      <p>Lorem ipsum dolor sit amet, consetetur sadipscing elitr, sed diam nonumy eirmod tempor invidunt ut labore et dolore magna aliquyam erat, sed diam voluptua.</p>
      <p>At vero eos et accusam et justo duo dolores et ea rebum. Stet clita kasd gubergren, no sea takim Lorem ipsum dolor sit amet, consetetur.</p>
    </article>
  </section>

  <section class="meet">
    <h2 class="meet-title">MEET US</h2>
    <div class="meet-text">
      <p>Lorem ipsum dolor sit amet, consetetur sadipscing elitr, sed diam nonumy eirmod tempor invidunt ut labore et dolore magna aliquyam erat, sed diam voluptua.</p>
      <p>At vero eos et accusam et justo duo dolores et ea rebum. Stet clita kasd gubergren, no sea takimata sanctus est Lorem ipsum dolor sit amet. Lorem ipsum dolor sit amet, conse, &nbsp;sed diam voluptua.</p>
      <p>At vero eos et accusam et justo duo dolores et ea rebum. Stet clita kasd gubergren, no sea takimata sanctus est Lorem ipsum dolor sit amet. Lorem ipsum dolor sit amet, consetetur dolore magna.</p>
    </div>
    <a class="read-more">Read More&gt;&gt;</a>
    <div class="portrait" role="img" aria-label="Round portrait placeholder of the company owner"></div>
  </section>

  <footer class="site-footer">
    <div class="footer-contact">
      <p>240 Sample Lane<br>Fairview, CA 94000</p>
      <p>office@quenbrickhall.com<br>415-555-0187</p>
    </div>
    <h3 class="galleries-title">Galleries</h3>
    <ul class="gallery-list" style="left:456px">
      <li>Additions</li><li>Renovations</li><li>Kitchens</li><li>Baths</li>
    </ul>
    <ul class="gallery-list" style="left:605px">
      <li>Finished Basements</li><li>Custom Wall Units</li><li>Decks</li><li>Millwork</li>
    </ul>
    <div class="social">
      <span class="social-square" role="img" aria-label="Social link"></span>
      <span class="social-square" role="img" aria-label="Email link"></span>
      <span class="social-square" role="img" aria-label="Social link"></span>
      <span class="social-square" role="img" aria-label="Social link"></span>
    </div>
    <p class="copyright">Copyright © 2016 Quenbrick Hall Construction</p>
  </footer>
</body>
</html>
```